kestrelnet9 - a safety solution for schools

A Amok App for schools needs your help to design some screens. Its important to have a very simple use of the app. The function of the app is very easy, you put the button to trigger the alarm. The app has a message function. So we need 3 howto screens. you find a better description of the project in the briefing-file. If you have any questions just ask. Thanks in advance for the suggestions. Best Regards, Lars

Target Market(s)

Schools

Industry/Entity Type

Security Service

Font styles to use
Sans Serif

Colors

Designer to choose colors to be used in the design.

Requirements
Must have
• Simple, easy to use, look like a security app, trust,

```html
<!DOCTYPE html>
<html lang="de">
<head>
<meta charset="utf-8">
<title>kestrelnet9 – App Screens</title>
<link href="https://fonts.googleapis.com/css2?family=Lato:wght@400;700&display=swap" rel="stylesheet">
<style>
  :root {
    --teal: #2ed6c6;
    --teal-light: #bff1ea;
    --pink: #ee0f72;
    --pink-deep: #e0186a;
    --pink-soft: #f7dbe8;
    --pink-softer: #f3c6da;
    --ink: #333a40;
    --muted: #a5adb3;
    --line: #cfd6da;
    --screen-bg: #f4f6fb;
    --white: #ffffff;
  }
  * { box-sizing: border-box; margin: 0; padding: 0; }
  html, body { width: 1200px; height: 720px; overflow: hidden; background: var(--white); }
  body { font-family: "Lato", sans-serif; color: var(--ink); }

  .stage { position: relative; width: 1200px; height: 720px; overflow: hidden; background: var(--white); }
  .blob { position: absolute; border-radius: 50%; }
  .blob--teal-large { left: -124px; top: -84px; width: 456px; height: 456px; background: var(--teal); }
  .blob--pink-top { left: 640px; top: 38px; width: 228px; height: 228px; background: var(--pink); }
  .blob--teal-small { left: 352px; top: 516px; width: 144px; height: 144px; background: var(--teal); }
  .blob--pink-large { left: 828px; top: 436px; width: 408px; height: 408px; background: var(--pink-deep); }

  .screen {
    position: absolute; top: 126px; width: 217px; height: 468px;
    background: linear-gradient(180deg, var(--white) 0%, var(--screen-bg) 100%);
    overflow: hidden; box-shadow: 0 18px 40px rgba(46, 214, 198, 0.12);
  }
  .screen--register { left: 32px; background: var(--white); }
  .screen--demo { left: 264px; }
  .screen--home { left: 496px; }
  .screen--active { left: 726px; }
  .screen--notified { left: 957px; }

  .status-bar {
    position: absolute; top: 10px; left: 0; right: 0; height: 12px; padding: 0 15px;
    display: flex; justify-content: space-between; align-items: center;
    font-size: 7.5px; font-weight: 700; color: var(--white); z-index: 3;
  }
  .screen--register .status-bar { color: #111; }
  .status-icons { display: flex; gap: 3px; align-items: center; }

  .header-arc {
    position: absolute; left: -31px; top: -140px; width: 279px; height: 282px;
    border-radius: 50%; background: var(--teal);
  }
  .header-content { position: absolute; left: 0; right: 0; text-align: center; color: var(--white); z-index: 2; }
  .demo-title { top: 61px; font-size: 13.5px; font-weight: 400; }
  .demo-text { top: 84px; font-size: 7px; line-height: 9.5px; }
  .nav { top: 64px; display: flex; justify-content: center; gap: 28px; }
  .nav-item { display: flex; flex-direction: column; align-items: center; gap: 4px; font-size: 6px; font-weight: 700; letter-spacing: .2px; width: 32px; }

  .alarm-label { position: absolute; top: 172px; left: 0; right: 0; text-align: center; font-size: 11px; font-weight: 400; color: var(--ink); }
  .alarm-button { position: absolute; left: 20px; top: 197px; width: 177px; height: 177px; }

  .cta {
    position: absolute; left: 41px; width: 134px; height: 38px;
    display: flex; align-items: center; justify-content: center;
    font-size: 8.5px; font-weight: 700; color: var(--white);
  }
  .cta--cancel { top: 399px; background: linear-gradient(90deg, var(--pink), #e8245e); }
  .cta--create { top: 387px; background: linear-gradient(90deg, #62dcf2, var(--teal)); font-weight: 400; }

  .illustration {
    position: absolute; left: 52px; top: 38px; width: 112px; height: 96px;
    border-radius: 50% 50% 46% 46%;
    background: radial-gradient(circle at 50% 45%, #eef5f6 0%, #f7fafb 60%, var(--white) 100%);
  }
  .register-title { position: absolute; top: 150px; left: 0; right: 0; text-align: center; font-size: 14px; color: var(--ink); }
  .register-text { position: absolute; top: 170px; left: 0; right: 0; text-align: center; font-size: 7px; line-height: 9.5px; color: var(--muted); }
  .field { position: absolute; left: 42px; width: 131px; height: 16px; border-bottom: 1px solid var(--line); font-size: 7.5px; color: #c3c9cd; padding-left: 11px; line-height: 12px; }
  .field--active { border-bottom-color: var(--teal); }
  .field--active::before { content: ""; position: absolute; left: 10px; top: 1px; width: 1px; height: 10px; background: #555; }

  .notification {
    position: absolute; left: 9px; top: 28px; width: 200px; height: 41px; z-index: 4;
    background: var(--teal-light); border-radius: 4px; padding: 6px 8px; color: #1b2a2a;
  }
  .notification-app { display: flex; align-items: center; gap: 5px; font-size: 6.5px; letter-spacing: .4px; }
  .notification-dot { width: 7px; height: 7px; border-radius: 50%; background: var(--pink); }
  .notification-time { position: absolute; right: 8px; top: 5px; font-size: 6px; color: #555; }
  .notification-title { margin-top: 4px; font-size: 6.5px; font-weight: 700; }
  .notification-body { font-size: 6.5px; }
</style>
</head>
<body>
<main class="stage">
  <div class="blob blob--teal-large"></div>
  <div class="blob blob--pink-top"></div>
  <div class="blob blob--teal-small"></div>
  <div class="blob blob--pink-large"></div>

  <svg width="0" height="0" style="position:absolute">
    <defs>
      <symbol id="icon-signal" viewBox="0 0 12 8"><rect x="0" y="5" width="2" height="3"/><rect x="3" y="3.5" width="2" height="4.5"/><rect x="6" y="2" width="2" height="6"/><rect x="9" y="0" width="2" height="8"/></symbol>
      <symbol id="icon-wifi" viewBox="0 0 12 9"><path d="M6 9 4 6.6a3 3 0 0 1 4 0z"/><path d="M2.5 5a5 5 0 0 1 7 0l-1 1.1a3.6 3.6 0 0 0-5 0z"/><path d="M.5 3a8 8 0 0 1 11 0l-1 1.1a6.6 6.6 0 0 0-9 0z"/></symbol>
      <symbol id="icon-battery" viewBox="0 0 18 8"><rect x=".5" y=".5" width="15" height="7" rx="1.5" fill="none" stroke="currentColor" opacity=".4"/><rect x="2" y="2" width="12" height="4" rx=".6"/><rect x="16.3" y="2.6" width="1.2" height="2.8" rx=".5"/></symbol>
      <symbol id="icon-gears" viewBox="0 0 24 24"><circle cx="9" cy="9" r="5" fill="none" stroke="currentColor" stroke-width="3" stroke-dasharray="2.2 1.4"/><circle cx="9" cy="9" r="2.2" fill="currentColor"/><circle cx="17" cy="17" r="3.5" fill="none" stroke="currentColor" stroke-width="2.4" stroke-dasharray="1.8 1.2"/><circle cx="17" cy="17" r="1.4" fill="currentColor"/></symbol>
      <symbol id="icon-message" viewBox="0 0 24 24"><path d="M12 3a9 9 0 1 1-4.6 16.7L3.5 21l1.3-3.7A9 9 0 0 1 12 3z" fill="none" stroke="currentColor" stroke-width="1.4"/><circle cx="8.3" cy="12" r="1" fill="currentColor"/><circle cx="12" cy="12" r="1" fill="currentColor"/><circle cx="15.7" cy="12" r="1" fill="currentColor"/></symbol>
      <symbol id="alarm" viewBox="0 0 177 177">
        <circle cx="88.5" cy="88.5" r="88" fill="#f9e3ed"/>
        <circle cx="88.5" cy="88.5" r="72" fill="#f4c9dc"/>
        <circle cx="88.5" cy="88.5" r="58" fill="none" stroke="#d80f57" stroke-width="3"/>
        <path d="M88.5 28.5a60 60 0 0 1 58 44" fill="none" stroke="#ee0f72" stroke-width="4" stroke-linecap="round"/>
        <circle cx="88.5" cy="88.5" r="53" fill="#ee0f72"/>
        <path d="M88.5 64 107 70v15c0 13-8 22-18.5 27C78 107 70 98 70 85V70z" fill="none" stroke="#fff" stroke-width="3.5" stroke-linejoin="round"/>
        <path d="M88.5 64 107 70v15c0 13-8 22-18.5 27z" fill="#fff"/>
      </symbol>
    </defs>
  </svg>

  <!-- Register -->
  <section class="screen screen--register">
    <div class="status-bar"><span>9:41</span>
      <span class="status-icons"><svg width="10" height="7" fill="currentColor"><use href="#icon-signal"/></svg><svg width="9" height="7" fill="currentColor"><use href="#icon-wifi"/></svg><svg width="14" height="7" fill="currentColor" color="#111"><use href="#icon-battery"/></svg></span>
    </div>
    <div class="illustration" role="img" aria-label="Illustration: Person auf einer Leiter setzt ein Häkchen an einen großen Schutzschild"></div>
    <h1 class="register-title">Register</h1>
    <p class="register-text">ed ut perspiciatis unde omnis<br>iste natus error</p>
    <div class="field field--active" style="top:224px">Name</div>
    <div class="field" style="top:259px">Vorname</div>
    <div class="field" style="top:294px">Email</div>
    <div class="field" style="top:329px">Schule</div>
    <div class="cta cta--create">Create Account</div>
  </section>

  <!-- Demo -->
  <section class="screen screen--demo">
    <div class="status-bar"><span>9:41</span>
      <span class="status-icons"><svg width="10" height="7" fill="currentColor"><use href="#icon-signal"/></svg><svg width="9" height="7" fill="currentColor"><use href="#icon-wifi"/></svg><svg width="14" height="7" fill="currentColor"><use href="#icon-battery"/></svg></span>
    </div>
    <div class="header-arc"></div>
    <h2 class="header-content demo-title">Demo Modus</h2>
    <p class="header-content demo-text">ed ut perspiciatis unde omnis<br>iste natus error</p>
    <p class="alarm-label">Schul-Alarm auslösen</p>
    <svg class="alarm-button"><use href="#alarm"/></svg>
  </section>

  <!-- Home -->
  <section class="screen screen--home">
    <div class="status-bar"><span>9:41</span>
      <span class="status-icons"><svg width="10" height="7" fill="currentColor"><use href="#icon-signal"/></svg><svg width="9" height="7" fill="currentColor"><use href="#icon-wifi"/></svg><svg width="14" height="7" fill="currentColor"><use href="#icon-battery"/></svg></span>
    </div>
    <div class="header-arc"></div>
    <nav class="header-content nav">
      <span class="nav-item"><svg width="20" height="20" color="#fff"><use href="#icon-gears"/></svg>SETTINGS</span>
      <span class="nav-item"><svg width="18" height="18" color="#fff"><use href="#icon-message"/></svg>MESSAGES</span>
    </nav>
    <p class="alarm-label">Schul-Alarm auslösen</p>
    <svg class="alarm-button"><use href="#alarm"/></svg>
  </section>

  <!-- Active alarm -->
  <section class="screen screen--active">
    <div class="status-bar"><span>9:41</span>
      <span class="status-icons"><svg width="10" height="7" fill="currentColor"><use href="#icon-signal"/></svg><svg width="9" height="7" fill="currentColor"><use href="#icon-wifi"/></svg><svg width="14" height="7" fill="currentColor"><use href="#icon-battery"/></svg></span>
    </div>
    <div class="header-arc"></div>
    <nav class="header-content nav">
      <span class="nav-item"><svg width="20" height="20" color="#fff"><use href="#icon-gears"/></svg>SETTINGS</span>
      <span class="nav-item"><svg width="18" height="18" color="#fff"><use href="#icon-message"/></svg>MESSAGES</span>
    </nav>
    <p class="alarm-label">Schul-Alarm auslösen</p>
    <svg class="alarm-button"><use href="#alarm"/></svg>
    <div class="cta cta--cancel">Cancel Alarm</div>
  </section>

  <!-- Notification -->
  <section class="screen screen--notified">
    <div class="status-bar"><span>9:41</span>
      <span class="status-icons"><svg width="10" height="7" fill="currentColor"><use href="#icon-signal"/></svg><svg width="9" height="7" fill="currentColor"><use href="#icon-wifi"/></svg><svg width="14" height="7" fill="currentColor"><use href="#icon-battery"/></svg></span>
    </div>
    <div class="header-arc"></div>
    <div class="notification">
      <div class="notification-app"><span class="notification-dot"></span>KESTRELNET9</div>
      <span class="notification-time">now</span>
      <p class="notification-title">Sekretariat</p>
      <p class="notification-body">Bitte bleiben Sie wo Sie sind</p>
    </div>
    <nav class="header-content nav">
      <span class="nav-item"><svg width="20" height="20" color="#fff"><use href="#icon-gears"/></svg>SETTINGS</span>
      <span class="nav-item"><svg width="18" height="18" color="#fff"><use href="#icon-message"/></svg>MESSAGES</span>
    </nav>
    <p class="alarm-label">Schul-Alarm auslösen</p>
    <svg class="alarm-button"><use href="#alarm"/></svg>
    <div class="cta cta--cancel">Cancel Alarm</div>
  </section>
</main>
</body>
</html>
```